Business card design needed for rebranded top-end landscaping business

We need a new business card design, incorporating our logo (colours Green #8dc63f and Grey #8a8c8e) and also some options that include the colour dark navy (eg #000040) as our uniforms are navy with white and grey trim.

We are an innovative landscaping company that maintains high-end gardens for meticulous clients. We pride ourselves on our customer service, our professionalism, and our workmanship.

Our business name needs to be easily read and our branding needs to be bold and memorable, without screaming "tradesman"! We prefer clean lines over lots of fine detail.

The design MUST include:
- Business name ("Brambleton Gardenworks")
- Logo (file uploaded)
- Employee name
- Phone number
- Email address
- www.brambletongardenworks.com.au
- Friendwall & Snapgrid logos
- The Turfcraft Guild logo (file uploaded) along with the word "Member"
- Licence "Lic. 618392K"

OPTIONAL inclusions:
- "Creating outdoor spaces for our community to be inspired, refreshed and re-energised"
- "Landscape Maintenance - Irrigation - Arboriculture" (dashes can be replaced with dots or other)
- "Fully qualified, licensed & insured"
- "Residential - Strata - Commercial - Real Estate" (dashes can be replaced with dots or other)

High-end professionals and retirees, real estate agents

Landscaping

See Project description

Sans Serif

Designer to choose colors to be used in the design.

• Must incorporate our logo, and colours Green #8dc63f and Grey #8a8c8e) from the logo, and the colour DARK NAVY (eg #000040).
• The design MUST include:
• - Business name ("Brambleton Gardenworks")
• - Logo (file uploaded)
• - Employee name
• - Phone number
• - Email address
• - www.brambletongardenworks.com.au
• - Friendwall & Snapgrid logos
• - The Turfcraft Guild logo (file uploaded) along with the word "Member"
• - Licence "Lic. 618392K"
• OPTIONAL inclusions:
• - "Creating outdoor spaces for our community to be inspired, refreshed and re-energised"
• - "Landscape Maintenance - Irrigation - Arboriculture" (dashes can be replaced with dots or other)
• - "Fully qualified, licensed & insured"
• - "Residential - Strata - Commercial - Real Estate" (dashes can be replaced with dots or other)

```html
<!DOCTYPE html>
<html lang="en">
<head>
<meta charset="utf-8">
<title>Brambleton Gardenworks – Business Card</title>
<link rel="stylesheet" href="https://fonts.googleapis.com/css2?family=Didact+Gothic&family=Poppins:wght@600&display=swap">
<style>
  :root{
    --page:#d0cbcb;
    --navy:#07062d;
    --ink:#0f0d3a;
    --green:#8dc63f;
    --grey:#8a8c8e;
    --heading:#2e2e33;
    --paper:#f6f6f6;
  }
  *{margin:0;padding:0;box-sizing:border-box}
  html,body{width:1200px;height:1200px;overflow:hidden}
  body{background:var(--page);font-family:"Didact Gothic",sans-serif;position:relative}

  .card{position:absolute;left:250px;width:700px;height:400px;overflow:hidden}
  .card--front{top:147px;background:var(--navy)}
  .card--back{top:652px;background:linear-gradient(135deg,#ffffff 0%,var(--paper) 55%,#ebebeb 100%)}

  /* front */
  .front-band{position:absolute;left:0;bottom:0;width:100%;height:12px;background:var(--green)}
  .brand{position:absolute;left:0;right:0;text-align:center}
  .brand__dot{display:block;margin:0 auto;border-radius:50%;background:var(--green)}
  .brand__name{font-family:"Poppins",sans-serif;font-weight:600;color:var(--grey);letter-spacing:.01em;line-height:1.15}
  .brand--front{top:78px}
  .brand--front .brand__dot{width:96px;height:96px;margin-bottom:26px}
  .brand--front .brand__name{font-size:38px}
  .front-url{position:absolute;left:0;right:0;top:354px;text-align:center;color:#a3a4ad;font-size:16px;letter-spacing:-.01em}

  /* back */
  .band{position:absolute;height:17px}
  .band--top-green{top:0;left:0;width:231px;background:var(--green)}
  .band--top-grey{top:0;left:231px;right:0;background:var(--grey)}
  .band--bottom-grey{bottom:0;left:0;width:324px;height:15px;background:var(--grey)}
  .band--bottom-green{bottom:0;left:324px;right:0;height:15px;background:var(--green)}

  .company{position:absolute;left:51px;top:56px;font-size:15px;color:var(--heading);letter-spacing:.01em}
  .contacts{position:absolute;left:50px;top:88px;list-style:none}
  .contacts li{display:flex;align-items:center;height:24px;font-size:14px;color:var(--ink);text-transform:uppercase}
  .contacts svg{width:16px;height:16px;margin-right:8px;fill:var(--ink)}

  .services{position:absolute;left:50px;top:200px;width:420px;list-style:none;color:var(--ink);font-size:14px;text-transform:uppercase}
  .services li{line-height:23px}
  .services li::before{content:"•";margin:0 10px 0 8px}
  .services .wrap{text-indent:0}

  .social{position:absolute;left:52px;top:330px;display:flex;gap:18px}
  .social__item{display:flex;align-items:center;gap:6px;font-size:12px;color:var(--ink)}
  .social__item span.sq{width:20px;height:20px;border-radius:3px;background:var(--ink)}

  .brand--back{top:58px;left:430px;right:0}
  .brand--back .brand__dot{width:54px;height:54px;margin-bottom:12px}
  .brand--back .brand__name{font-size:19px}

  .member-badge{position:absolute;left:522px;top:262px;width:80px;height:80px;border-radius:6px;background:var(--grey)}
</style>
</head>
<body>

<section class="card card--front">
  <div class="brand brand--front">
    <span class="brand__dot"></span>
    <div class="brand__name">Brambleton<br>Gardenworks</div>
  </div>
  <div class="front-url">WWW.BRAMBLETONGARDENWORKS.COM.AU</div>
  <div class="front-band"></div>
</section>

<section class="card card--back">
  <div class="band band--top-green"></div>
  <div class="band band--top-grey"></div>

  <h2 class="company">BRAMBLETON GARDENWORKS</h2>

  <ul class="contacts">
    <li>
      <svg viewBox="0 0 24 24" aria-hidden="true"><path d="M6.6 10.8a15.1 15.1 0 0 0 6.6 6.6l2.2-2.2c.3-.3.7-.4 1-.2 1.1.4 2.3.6 3.6.6.6 0 1 .4 1 1V20c0 .6-.4 1-1 1A17 17 0 0 1 3 4c0-.6.4-1 1-1h3.5c.6 0 1 .4 1 1 0 1.3.2 2.5.6 3.6.1.3 0 .7-.2 1z"/></svg>
      0491 570 318
    </li>
    <li>
      <svg viewBox="0 0 24 24" aria-hidden="true"><path d="M2 5h20v14H2z M3.5 6.5 12 13l8.5-6.5" fill="none" stroke="#0f0d3a" stroke-width="1.8"/><path d="M2 5h20L12 13z"/></svg>
      PO Box 5102 Millbrook, NSW, 2577
    </li>
    <li>
      <svg viewBox="0 0 24 24" aria-hidden="true"><path d="M22 2 2 10l7 3 2 8 3-6 6 4z"/></svg>
      info@brambletongardenworks.com.au
    </li>
    <li>
      <svg viewBox="0 0 24 24" aria-hidden="true"><path d="M5 2h10l4 4v9h-2V7h-3V4H7v16h6v2H5z"/><circle cx="17" cy="18" r="3"/></svg>
      Lic. 618392K
    </li>
  </ul>

  <ul class="services">
    <li>Creating outdoor spaces for our community to be inspired, refreshed and re-energised</li>
    <li>Landscape Maintenance &nbsp;• Irrigation &nbsp;• Arboriculture</li>
    <li>Fully qualified, licensed &amp; insured</li>
    <li>Residential &nbsp;• Strata &nbsp;• Commercial &nbsp;• Real Estate</li>
  </ul>

  <div class="social">
    <div class="social__item"><span class="sq"></span>Friendwall</div>
    <div class="social__item"><span class="sq"></span>Snapgrid</div>
  </div>

  <div class="brand brand--back">
    <span class="brand__dot"></span>
    <div class="brand__name">Brambleton<br>Gardenworks</div>
  </div>

  <div class="member-badge" role="img" aria-label="The Turfcraft Guild member badge"></div>

  <div class="band band--bottom-grey"></div>
  <div class="band band--bottom-green"></div>
</section>

</body>
</html>
```